Craft brewery keg badge / badge branding to be on display on keg fonts in pubs and craft beer bars

We're a small craft beer producer and are looking to have a keg badge designed to be put onto keg fonts in bars as well as being used on our bottles. Our website is www.qelmarbrewing.co.uk. -Please take a look at our site however we're looking for new branding! We're not looking to have the windmill on the badge! We want a bold geometric hop design in the centre of the design. The beer is a low AVB beer (2.9% ABV) and will be hopped with Cascade, Colombus and Mosaic hops and will have a fruity / juicy aroma. We're looking to have a design that we can re-use again and again by changing: colours and wording for different beers in the future.

Target Market(s)
Craft beer drinkers
Industry/Entity Type
Craft Brewery
Requirements
Must have
- Simple, elegant, repeatable core message from the badge. It need a simple, bold geometric hop design (examples uploaded) in the centre which is repeatable across many brands in the future.
- The badge needs to be circular and 82mm across to fit our tap lenses (see http://www.drevix.co.uk/branding for the flat lens). The keg badge needs to be modern and in line with other keg badges like the examples attached- though we leave the artistic flair up to you guys. Please see below the styles of keg badge we like.
- Must be in vector file format and we must get a jpeg version too.

Should not have
- Should not be overcrowded and try to be too full of information. See attached examples.

```html
<!DOCTYPE html>
<html lang="en">
<head>
<meta charset="utf-8">
<title>Keg Badge Colourways</title>
<link rel="stylesheet" href="https://fonts.googleapis.com/css2?family=Montserrat:wght@700;800;900&display=swap">
<style>
  :root {
    --canvas: #fffcb6;
    --badge-white: #ffffff;
    --ink: #111111;
    --amber-light: #fdd27e;
    --amber-deep: #f3bd5c;
    --slate: #5b5a56;
    --slate-shadow: #4a4a48;
    --night: #050505;
    --ale: #6b5520;
    --foam: #cfcfc9;
    --ocean-light: #3c7191;
    --ocean-deep: #0f2c55;
    --hop-green-top: #6af04a;
    --hop-green-bottom: #4fb83c;
    --hop-yellow-top: #f8ec52;
    --hop-yellow-bottom: #f6b53a;
    --hop-dark: rgba(40, 30, 10, 0.55);
  }
  * { box-sizing: border-box; margin: 0; padding: 0; }
  html, body { width: 1200px; height: 1200px; overflow: hidden; }
  body { background: var(--canvas); position: relative; font-family: "Montserrat", sans-serif; }

  .badge {
    position: absolute;
    width: 480px; height: 480px;
    border-radius: 50%;
    background: var(--badge-white);
  }
  .badge--amber  { left: 60px;  top: 52px; }
  .badge--slate  { left: 661px; top: 54px; }
  .badge--pint   { left: 62px;  top: 652px; }
  .badge--glacier{ left: 662px; top: 654px; }

  .badge__face {
    position: absolute;
    left: 13px; top: 13px;
    width: 454px; height: 454px;
    border-radius: 50%;
    overflow: hidden;
    background: var(--badge-white);
  }
  .badge__art {
    position: absolute;
    left: 0; top: 0;
    width: 100%; height: 371px;
  }
  .badge--amber .badge__art {
    background: radial-gradient(circle at 50% 45%, var(--amber-light) 0%, var(--amber-light) 55%, var(--amber-deep) 100%);
  }
  .badge--slate .badge__art { background: var(--slate); }
  .badge--slate .badge__shadow {
    position: absolute; inset: 0;
    background: linear-gradient(135deg, transparent 0%, transparent 50%, var(--slate-shadow) 50%, var(--slate-shadow) 100%);
    clip-path: polygon(54% 30%, 100% 74%, 100% 100%, 54% 100%, 38% 100%);
    opacity: 0.9;
  }
  .badge--pint .badge__art {
    background:
      linear-gradient(180deg, var(--night) 0%, var(--night) 12%, var(--foam) 24%, #8d8a7c 42%, var(--ale) 62%, #3a2c0c 100%);
  }
  .badge--glacier .badge__art {
    background: linear-gradient(160deg, var(--ocean-light) 0%, #22507a 45%, var(--ocean-deep) 100%);
  }

  .hop {
    position: absolute;
    left: 50%;
    transform: translateX(-50%);
    top: 43px;
    width: 150px; height: 288px;
    border: 4px solid var(--badge-white);
    border-radius: 40% 40% 50% 50% / 30% 30% 70% 70%;
  }
  .hop--green  { background: linear-gradient(180deg, var(--hop-green-top), var(--hop-green-bottom)); }
  .hop--yellow { background: linear-gradient(180deg, var(--hop-yellow-top), var(--hop-yellow-bottom)); }
  .hop--dark   { background: var(--hop-dark); }

  .badge__label {
    position: absolute;
    left: 0; right: 0;
    top: 393px;
    text-align: center;
    color: var(--ink);
  }
  .badge__name {
    display: inline-block;
    font-weight: 900;
    font-size: 22px;
    letter-spacing: 0.3px;
    line-height: 1;
    padding: 0 20px 3px;
    border-bottom: 1.5px solid var(--ink);
  }
  .badge__brewery {
    font-weight: 700;
    font-size: 10.5px;
    margin-top: 6px;
    letter-spacing: 0.2px;
  }
  .badge__abv {
    font-weight: 700;
    font-size: 10.5px;
    margin-top: 15px;
  }
</style>
</head>
<body>

  <div class="badge badge--amber">
    <div class="badge__face">
      <div class="badge__art" role="img" aria-label="Amber background with soft wavy pattern"></div>
      <div class="hop hop--green" role="img" aria-label="Bold geometric hop cone in green"></div>
    </div>
    <div class="badge__label">
      <div class="badge__name">BRAND NAME</div>
      <div class="badge__brewery">QELMAR BREWING CO. LTD</div>
      <div class="badge__abv">2.9% ABV</div>
    </div>
  </div>

  <div class="badge badge--slate">
    <div class="badge__face">
      <div class="badge__art"><div class="badge__shadow"></div></div>
      <div class="hop hop--yellow" role="img" aria-label="Bold geometric hop cone in yellow"></div>
    </div>
    <div class="badge__label">
      <div class="badge__name">BRAND NAME</div>
      <div class="badge__brewery">QELMAR BREWING CO. LTD</div>
      <div class="badge__abv">2.9% ABV</div>
    </div>
  </div>

  <div class="badge badge--pint">
    <div class="badge__face">
      <div class="badge__art" role="img" aria-label="Photograph of a foaming glass of beer on black"></div>
      <div class="hop hop--dark" role="img" aria-label="Bold geometric hop cone in white outline"></div>
    </div>
    <div class="badge__label">
      <div class="badge__name">BRAND NAME</div>
      <div class="badge__brewery">QELMAR BREWING CO. LTD</div>
      <div class="badge__abv">2.9% ABV</div>
    </div>
  </div>

  <div class="badge badge--glacier">
    <div class="badge__face">
      <div class="badge__art" role="img" aria-label="Blue low-poly faceted background"></div>
      <div class="hop hop--yellow" role="img" aria-label="Bold geometric hop cone in yellow"></div>
    </div>
    <div class="badge__label">
      <div class="badge__name">BRAND NAME</div>
      <div class="badge__brewery">QELMAR BREWING CO. LTD</div>
      <div class="badge__abv">2.9% ABV</div>
    </div>
  </div>

</body>
</html>
```